Flyer Template

I need a flyer template for door knocking on properties. Text Boxes need to be editable, with a header and text body. Footer to be my info. Project to be stylized to match my real estate signs and logo art from past projects

```html
<!DOCTYPE html>
<html lang="en">
<head>
<meta charset="utf-8">
<title>Marlowe Realty – Home Buying Flyer</title>
<link rel="stylesheet" href="https://fonts.googleapis.com/css2?family=Oswald:wght@500;700&family=Lato:wght@400;700&display=swap">
<style>
  :root {
    --stage: #8a8a8a;
    --paper: #ffffff;
    --brand-red: #e8473a;
    --brand-red-deep: #d9372c;
    --ink: #0b0b0b;
    --panel-grey: #e6e6e6;
    --white: #ffffff;
    --headline-font: "Oswald", "Arial Narrow", sans-serif;
    --body-font: "Lato", "Helvetica Neue", Arial, sans-serif;
  }
  * { box-sizing: border-box; margin: 0; padding: 0; }
  html, body { width: 1200px; height: 1200px; overflow: hidden; }
  body { background: var(--stage); position: relative; font-family: var(--body-font); }

  .flyer {
    position: absolute; left: 181px; top: 38px;
    width: 861px; height: 1105px;
    background: var(--paper); overflow: hidden;
    box-shadow: 4px 6px 14px rgba(0,0,0,.35);
  }
  .hero-photo {
    position: absolute; left: 0; top: 0; width: 861px; height: 570px;
    background: linear-gradient(160deg, #4d6a96 0%, #c9a88a 35%, #6d5a55 60%, #4a4030 100%);
  }
  .hero-overlay { position: absolute; left: 0; top: 0; width: 861px; height: 570px; }

  .brand-name {
    position: absolute; left: 24px; top: 300px; width: 140px;
    font-family: var(--body-font); font-weight: 700; color: var(--white);
    font-size: 24px; line-height: 38px; text-align: center; letter-spacing: .5px;
  }
  .brand-square {
    position: absolute; left: 67px; top: 232px; width: 54px; height: 54px;
    background: var(--white);
  }

  .headline-lead {
    position: absolute; left: 173px; top: 203px;
    font-family: var(--headline-font); font-weight: 700; color: var(--white);
    font-size: 48px; line-height: 1;
  }
  .headline-main {
    position: absolute; left: 173px; top: 256px;
    font-family: var(--headline-font); font-weight: 700; color: var(--white);
    font-size: 70px; line-height: 1;
  }
  .headline-tag {
    position: absolute; left: 176px; top: 335px; width: 374px; height: 62px;
    background: var(--white); color: var(--ink);
    font-family: var(--body-font); font-weight: 700; font-size: 46px;
    line-height: 62px; text-align: center;
  }
  .hero-intro {
    position: absolute; left: 35px; top: 419px; width: 520px;
    color: var(--white); font-size: 15.5px; line-height: 20px;
  }

  .services-title {
    position: absolute; left: 0; top: 494px; width: 361px; height: 84px;
    background: var(--ink); color: var(--white);
    font-family: var(--headline-font); font-weight: 700; font-size: 50px;
    line-height: 84px; padding-left: 23px;
  }
  .services-list {
    position: absolute; top: 589px; list-style: none;
    font-size: 15px; color: var(--ink);
  }
  .services-list.col-a { left: 37px; }
  .services-list.col-b { left: 259px; }
  .services-list li { height: 27.4px; line-height: 22px; display: flex; align-items: center; gap: 8px; }
  .services-list svg { width: 14px; height: 14px; flex: none; }

  .services-note {
    position: absolute; left: 37px; top: 836px; width: 410px;
    font-size: 16px; line-height: 20px; color: var(--ink);
  }

  .agent-panel {
    position: absolute; left: 478px; top: 573px; width: 358px; height: 335px;
    background: var(--panel-grey);
  }
  .agent-photo { position: absolute; left: 500px; top: 429px; width: 320px; height: 320px; }
  .agent-name {
    position: absolute; left: 478px; top: 760px; width: 358px; text-align: center;
    font-family: var(--headline-font); font-weight: 500; color: var(--brand-red);
    font-size: 52px; line-height: 1;
  }
  .agent-contact {
    position: absolute; left: 545px; font-size: 24px; font-weight: 400;
    color: var(--ink); display: flex; align-items: center; gap: 10px; line-height: 1;
  }
  .agent-contact.phone { top: 828px; }
  .agent-contact.email { top: 862px; }
  .agent-contact svg { width: 22px; height: 22px; }

  .property-bar {
    position: absolute; left: 24px; top: 932px; width: 811px; height: 148px;
    background: var(--ink); color: var(--white);
  }
  .bar-heading {
    position: absolute; top: 19px;
    font-family: var(--headline-font); font-weight: 500; font-size: 18px; letter-spacing: .2px;
  }
  .bar-text { position: absolute; top: 57px; width: 190px; font-size: 12px; line-height: 15px; }
  .bar-divider { position: absolute; top: 24px; width: 2px; height: 103px; background: var(--white); }
  .about .bar-heading { left: 54px; }
  .about .bar-text { left: 45px; }
  .features .bar-heading { left: 328px; }
  .features .bar-text { left: 324px; top: 58px; }
  .prices { position: absolute; left: 630px; top: 0; width: 130px; text-align: center; }
  .prices .bar-heading { left: 0; width: 130px; }
  .price-line { position: absolute; left: 0; width: 130px; font-size: 15px; }

  .footer-band {
    position: absolute; left: 0; top: 1092px; width: 861px; height: 13px;
    background: var(--brand-red);
  }
</style>
</head>
<body>
  <main class="flyer">
    <div class="hero-photo" role="img" aria-label="Photograph of modern apartment buildings at dusk with a lit brick courtyard"></div>
    <svg class="hero-overlay" viewBox="0 0 861 570" aria-hidden="true">
      <defs>
        <linearGradient id="redWash" x1="0" y1="0" x2="1" y2="1">
          <stop offset="0" stop-color="#e8473a" stop-opacity=".95"/>
          <stop offset="1" stop-color="#d9372c" stop-opacity=".9"/>
        </linearGradient>
      </defs>
      <polygon points="0,183 558,183 590,477 861,477 861,570 0,570" fill="url(#redWash)"/>
    </svg>

    <div class="brand-square" aria-hidden="true"></div>
    <div class="brand-name">MARLOWE<br>REALTY</div>

    <h1 class="headline-lead">The First steps to</h1>
    <div class="headline-main">HOME BUYING</div>
    <div class="headline-tag">LOREM IPSUM</div>
    <p class="hero-intro">Lorem ipsum dolor sit amet, consectetur adipiscing elit, sed do eiusmod tempor incididunt ut labore et dolore magna aliqua.</p>

    <h2 class="services-title">OUR SERVICES</h2>
    <ul class="services-list col-a">
      <li><svg viewBox="0 0 14 14"><path d="M2 7.5l3 3 7-7" fill="none" stroke="#e8473a" stroke-width="2.2"/></svg>Lorem ipsum</li>
      <li><svg viewBox="0 0 14 14"><path d="M2 7.5l3 3 7-7" fill="none" stroke="#e8473a" stroke-width="2.2"/></svg>dolor sit amet</li>
      <li><svg viewBox="0 0 14 14"><path d="M2 7.5l3 3 7-7" fill="none" stroke="#e8473a" stroke-width="2.2"/></svg>consectetur adipiscing elit</li>
      <li><svg viewBox="0 0 14 14"><path d="M2 7.5l3 3 7-7" fill="none" stroke="#e8473a" stroke-width="2.2"/></svg>sed do eiusmod tempor</li>
      <li><svg viewBox="0 0 14 14"><path d="M2 7.5l3 3 7-7" fill="none" stroke="#e8473a" stroke-width="2.2"/></svg>incididunt ut labore et</li>
      <li><svg viewBox="0 0 14 14"><path d="M2 7.5l3 3 7-7" fill="none" stroke="#e8473a" stroke-width="2.2"/></svg>dolore magna aliqua.</li>
      <li><svg viewBox="0 0 14 14"><path d="M2 7.5l3 3 7-7" fill="none" stroke="#e8473a" stroke-width="2.2"/></svg>Ut enim ad minim</li>
      <li><svg viewBox="0 0 14 14"><path d="M2 7.5l3 3 7-7" fill="none" stroke="#e8473a" stroke-width="2.2"/></svg>veniam, quis nostrud</li>
    </ul>
    <ul class="services-list col-b">
      <li><svg viewBox="0 0 14 14"><path d="M2 7.5l3 3 7-7" fill="none" stroke="#e8473a" stroke-width="2.2"/></svg>exercitation ullamco</li>
      <li><svg viewBox="0 0 14 14"><path d="M2 7.5l3 3 7-7" fill="none" stroke="#e8473a" stroke-width="2.2"/></svg>laboris nisi ut aliquip</li>
      <li><svg viewBox="0 0 14 14"><path d="M2 7.5l3 3 7-7" fill="none" stroke="#e8473a" stroke-width="2.2"/></svg>ex ea commodo consequat</li>
      <li><svg viewBox="0 0 14 14"><path d="M2 7.5l3 3 7-7" fill="none" stroke="#e8473a" stroke-width="2.2"/></svg>Duis aute irure dolor</li>
      <li><svg viewBox="0 0 14 14"><path d="M2 7.5l3 3 7-7" fill="none" stroke="#e8473a" stroke-width="2.2"/></svg>in reprehenderit in</li>
      <li><svg viewBox="0 0 14 14"><path d="M2 7.5l3 3 7-7" fill="none" stroke="#e8473a" stroke-width="2.2"/></svg>voluptate velit esse</li>
      <li><svg viewBox="0 0 14 14"><path d="M2 7.5l3 3 7-7" fill="none" stroke="#e8473a" stroke-width="2.2"/></svg>cillum dolore eu fugiat</li>
      <li><svg viewBox="0 0 14 14"><path d="M2 7.5l3 3 7-7" fill="none" stroke="#e8473a" stroke-width="2.2"/></svg>nulla pariatur</li>
    </ul>
    <p class="services-note">Lorem ipsum dolor sit amet, consectetur adipiscing elit, sed do eiusmod tempor incididunt ut labore et dolore magna aliqua.</p>

    <div class="agent-panel"></div>
    <svg class="agent-photo" viewBox="0 0 320 320" role="img" aria-label="Portrait photograph of the real estate agent">
      <defs>
        <linearGradient id="portraitTone" x1="0" y1="0" x2="0" y2="1">
          <stop offset="0" stop-color="#c9c9c7"/>
          <stop offset=".65" stop-color="#b9b8b5"/>
          <stop offset="1" stop-color="#b7cde0"/>
        </linearGradient>
      </defs>
      <circle cx="160" cy="160" r="157" fill="url(#portraitTone)" stroke="#0b0b0b" stroke-width="5"/>
    </svg>
    <div class="agent-name">Jordan Marlowe</div>
    <div class="agent-contact phone">
      <svg viewBox="0 0 22 22" aria-hidden="true"><circle cx="11" cy="11" r="9.5" fill="none" stroke="#e8473a" stroke-width="1.6"/><path d="M7.5 6.5l2 0 1 2.5-1.3 1a6 6 0 0 0 2.8 2.8l1-1.3 2.5 1v2a1 1 0 0 1-1 1A8 8 0 0 1 6.5 7.5a1 1 0 0 1 1-1z" fill="#e8473a"/></svg>
      555-014-0288
    </div>
    <div class="agent-contact email">
      <svg viewBox="0 0 22 22" aria-hidden="true"><rect x="1" y="4" width="20" height="14" fill="#e8473a"/><path d="M1 4l10 8 10-8M1 18l7-7M21 18l-7-7" fill="none" stroke="#fff" stroke-width="1.4"/></svg>
      jmarlowe@example.com
    </div>

    <section class="property-bar">
      <div class="about">
        <h3 class="bar-heading">ABOUT THE PROPERTY</h3>
        <p class="bar-text">Lorem ipsum dolor sit amet, consectetur adipiscing elit, sed do eiusmod tempor incididunt ut labore et dolore magna aliqua. Ut enim ad</p>
      </div>
      <div class="bar-divider" style="left:273px"></div>
      <div class="features">
        <h3 class="bar-heading">PROPERTY FEATURES</h3>
        <p class="bar-text">Lorem ipsum dolor sit amet, consectetur adipiscing elit, sed do eiusmod tempor incididunt ut labore et dolore magna aliqua. Ut enim ad</p>
      </div>
      <div class="bar-divider" style="left:559px"></div>
      <div class="prices">
        <h3 class="bar-heading">PRICES</h3>
        <div class="price-line" style="top:58px">$ 1,000.00</div>
        <div class="price-line" style="top:84px">$ 2,000.00</div>
      </div>
    </section>

    <div class="footer-band"></div>
  </main>
</body>
</html>
```